Digital Marketing company needs business cards

We are a digital marketing company providing SEO, Bidlane and Web Development services in Australia and New Zealand. Colours and icons have to match the current website (kestrelworks.com.au). We'd like to keep the cards simple and clean, using the artwork we have as the background of the slider of the website (the triangles). The card should have horizontal layout.
If we could have our core services on the reverse side that'd be great:
SEO
BidLane
Web Design&Development
Target Market(s)
Medium size to large businesses
Industry/Entity Type
Digital

```html
<!DOCTYPE html>
<html lang="en">
<head>
<meta charset="utf-8">
<title>KestrelWorks – Business Cards</title>
<link rel="stylesheet" href="https://fonts.googleapis.com/css2?family=Montserrat:wght@700&family=Questrial&display=swap">
<style>
  :root {
    --page: #eceef1;
    --card-light: #eceeef;
    --blue-deep: #1f4fb8;
    --blue-mid: #3a6fd6;
    --blue-soft: #8fb0ea;
    --ink: #3b3f45;
    --ink-strong: #2d3a4e;
    --name-grey: #9ea5ae;
    --white: #ffffff;
  }
  * { box-sizing: border-box; margin: 0; padding: 0; }
  html, body { width: 1200px; height: 900px; overflow: hidden; }
  body {
    background: var(--page);
    font-family: "Questrial", "Century Gothic", sans-serif;
    position: relative;
  }
  .card {
    position: absolute;
    top: 285px;
    width: 540px;
    height: 330px;
    overflow: hidden;
    box-shadow: 0 8px 24px rgba(30, 40, 60, 0.18);
  }
  .card--front { left: 40px; background: var(--card-light); }
  .card--back { left: 620px; background: var(--blue-mid); }
  .card__art { position: absolute; inset: 0; }

  /* front */
  .brand {
    position: absolute;
    left: 24px;
    top: 20px;
    display: flex;
    align-items: center;
    gap: 10px;
    font-size: 34px;
    letter-spacing: -0.5px;
    color: var(--ink);
  }
  .brand__dot {
    width: 26px; height: 26px;
    border-radius: 50%;
    background: var(--blue-mid);
  }
  .contact {
    position: absolute;
    left: 30px;
    top: 172px;
    width: 240px;
    list-style: none;
    text-align: right;
    color: var(--white);
    font-size: 14px;
    line-height: 22px;
  }
  .contact li { display: flex; justify-content: flex-end; align-items: center; gap: 10px; }
  .contact__icon { width: 20px; height: 20px; flex: none; }
  .contact__spacer { width: 20px; flex: none; }
  .person {
    position: absolute;
    left: 300px;
    top: 108px;
  }
  .person__name {
    font-size: 25px;
    line-height: 30px;
    color: var(--name-grey);
    letter-spacing: 0.3px;
  }
  .person__role {
    margin-top: 2px;
    font-family: "Montserrat", "Century Gothic", sans-serif;
    font-weight: 700;
    font-size: 13px;
    line-height: 16px;
    color: var(--ink-strong);
  }

  /* back */
  .web {
    position: absolute;
    left: 26px;
    top: 232px;
    color: var(--white);
    font-size: 16px;
    letter-spacing: 3px;
  }
  .back-brand {
    position: absolute;
    right: 28px;
    top: 148px;
    display: flex;
    align-items: center;
    gap: 10px;
    color: var(--white);
    font-size: 30px;
    letter-spacing: -0.5px;
  }
  .back-brand__dot {
    width: 24px; height: 24px;
    border-radius: 50%;
    background: var(--white);
  }
</style>
</head>
<body>

<section class="card card--front" aria-label="Business card, front">
  <svg class="card__art" width="540" height="330" viewBox="0 0 540 330">
    <defs>
      <linearGradient id="frontPattern" x1="0" y1="0" x2="1" y2="1">
        <stop offset="0" stop-color="#5f8de0"/>
        <stop offset="0.5" stop-color="#2f62cc"/>
        <stop offset="1" stop-color="#5a84d6"/>
      </linearGradient>
    </defs>
    <polygon points="0,75 540,255 540,330 0,330" fill="url(#frontPattern)" role="img" aria-label="Blue faceted triangle pattern"/>
    <polygon points="0,292 540,302 540,306 0,296" fill="var(--white)"/>
    <rect x="0" y="305" width="540" height="25" fill="var(--blue-soft)" opacity="0.85"/>
  </svg>

  <div class="brand"><span class="brand__name">kestrelworks</span><span class="brand__dot"></span></div>

  <ul class="contact">
    <li><span>+1 555.210.4410</span><span class="contact__spacer"></span></li>
    <li><span>+1 555.210.4411</span>
      <svg class="contact__icon" viewBox="0 0 20 20"><circle cx="10" cy="10" r="9" fill="none" stroke="#fff" stroke-width="1.5"/><path d="M6.5 5.5l2 2-1 1.5c.8 1.6 2 2.8 3.5 3.5l1.5-1 2 2-1.5 1.5c-3.5-.5-7-4-7.5-7.5z" fill="#fff"/></svg></li>
    <li><span>marina@kestrelworks.com.au</span>
      <svg class="contact__icon" viewBox="0 0 20 20"><circle cx="10" cy="10" r="9" fill="none" stroke="#fff" stroke-width="1.5"/><rect x="7" y="5" width="6" height="10" rx="1" fill="none" stroke="#fff" stroke-width="1.4"/><circle cx="10" cy="13" r="0.8" fill="#fff"/></svg></li>
    <li><span>KestrelWorks, Streetname 123</span>
      <svg class="contact__icon" viewBox="0 0 20 20"><circle cx="10" cy="10" r="9" fill="none" stroke="#fff" stroke-width="1.5"/><rect x="5.5" y="6.5" width="9" height="7" fill="none" stroke="#fff" stroke-width="1.3"/><path d="M5.5 6.5l4.5 4 4.5-4" fill="none" stroke="#fff" stroke-width="1.3"/></svg></li>
    <li><span>State ZIP code 123456</span>
      <svg class="contact__icon" viewBox="0 0 20 20"><circle cx="10" cy="10" r="9" fill="none" stroke="#fff" stroke-width="1.5"/><path d="M10 15.5s-3.5-3.8-3.5-6.3a3.5 3.5 0 0 1 7 0c0 2.5-3.5 6.3-3.5 6.3z" fill="none" stroke="#fff" stroke-width="1.3"/><circle cx="10" cy="9.2" r="1.2" fill="#fff"/></svg></li>
  </ul>

  <div class="person">
    <p class="person__name">Marina Holt</p>
    <p class="person__role">Director</p>
  </div>
</section>

<section class="card card--back" aria-label="Business card, back">
  <svg class="card__art" width="540" height="330" viewBox="0 0 540 330">
    <defs>
      <linearGradient id="backPattern" x1="0" y1="0" x2="1" y2="1">
        <stop offset="0" stop-color="#cdd9f0"/>
        <stop offset="0.25" stop-color="#4f7fdc"/>
        <stop offset="0.6" stop-color="#2a5ccb"/>
        <stop offset="1" stop-color="#3f6fd4"/>
      </linearGradient>
    </defs>
    <rect width="540" height="330" fill="url(#backPattern)" role="img" aria-label="Blue faceted triangle pattern"/>
    <polygon points="0,0 150,0 0,90" fill="var(--card-light)" opacity="0.9"/>
    <rect x="0" y="262" width="540" height="4" fill="var(--white)"/>
    <rect x="0" y="266" width="540" height="64" fill="var(--blue-deep)"/>
  </svg>
  <p class="web">www.kestrelworks.com.au</p>
  <div class="back-brand"><span>kestrelworks</span><span class="back-brand__dot"></span></div>
</section>

</body>
</html>
```